Catchy Cards for Hospital

I run a rural hospital in Texas called Pelham Ridge Hospital and am in need of contemporary business cards for all of my Department Heads. While our logo is somewhat simplistic, I don't have the option of changing it at this time, so anything to make the rest of the card present the appearance of a modern, professional healthcare facility would be great. Although the attached files are in black, our hospital colors are in a copper brown and black. I need to be able to change the name and title on the card so I can get cards printed for various department heads.

Target Market(s)

Referring physicians, large hospital systems, national organizations, state and federal government

Industry/Entity Type

Hospital

Contact Information for Business Card

Name Derek Solano
Title CEO

Phone: Main 325-740-2386 & Direct xxxxxx
Fax xxxxx
derek.solano@pelhamrh.com
382 Wilmot Street Box 415
Alder Springs, Westmark 76291

Font styles to use
Serif

Colors
f48340

Requirements
Must have
• Clean crisp lines and ability to modify names, titles and emails
• On the back "PelhamRidgeHospital.Com
Nice to have
• Needs to be in line with logo, which is a bit dated and not too appealing, but I'm hoping that the rest of the card can make up for that fact just a little bit.
• Hospital's colors are a copper brown, black and white
Should not have
• Shapes or anything distracting

```html
<!DOCTYPE html>
<html lang="en">
<head>
<meta charset="utf-8">
<title>Pelham Ridge Hospital Stationery</title>
<link href="https://fonts.googleapis.com/css2?family=Hind:wght@400;600;700&display=swap" rel="stylesheet">
<style>
:root{
  --copper:#8b4a38;
  --ink:#3a3a3c;
  --paper:#ffffff;
  --backdrop:#a7a7a6;
  --shade:rgba(0,0,0,.28);
}
*{margin:0;padding:0;box-sizing:border-box}
html,body{width:1200px;height:838px;overflow:hidden}
body{background:var(--backdrop);font-family:'Hind',Arial,sans-serif;color:#111;position:relative}
.piece{position:absolute;background:var(--paper);box-shadow:2px 3px 8px var(--shade);overflow:hidden}
.piece svg.wave{position:absolute;left:0;width:100%}
.brand{font-family:'Hind',Arial,sans-serif;font-weight:700;color:var(--copper);line-height:.95}

/* business card back */
.card-back{left:169px;top:88px;width:203px;height:118px;background:var(--copper)}
.card-back .brand{color:#fff;position:absolute;left:52px;top:32px;font-size:19px;width:110px}

/* business card front */
.card-front{left:389px;top:88px;width:203px;height:118px}
.card-front .brand{position:absolute;left:14px;top:30px;font-size:12px;width:72px}
.card-front .divider{position:absolute;left:93px;top:8px;width:1px;height:62px;background:var(--copper)}
.card-front .info{position:absolute;left:100px;top:8px;font-size:5.3px;line-height:1.35;color:#222}
.card-front .name{font-size:8px;font-weight:700;color:var(--copper);letter-spacing:.4px}
.card-front .title{font-weight:600;margin-bottom:5px}
.card-front .addr{margin-bottom:4px}
.contact-row{display:flex;align-items:center;gap:3px}
.dot{width:4px;height:4px;border-radius:50%;background:var(--copper);display:inline-block}
.card-front .wave{bottom:0;height:36px}

/* envelope front */
.env-front{left:109px;top:231px;width:480px;height:242px}
.env-front .brand{position:absolute;left:24px;top:22px;font-size:15px;width:90px}
.env-front .addr{position:absolute;left:28px;top:78px;font-size:5.8px;line-height:1.35;font-weight:600}
.env-front .wave{bottom:0;height:62px}

/* envelope back */
.env-back{left:109px;top:503px;width:480px;height:247px;background:linear-gradient(180deg,#fff 40%,#f1f1f1)}
.env-back .flap{position:absolute;left:0;top:0;width:100%;height:68px}
.env-back .brand{position:absolute;left:190px;top:13px;font-size:16px;width:110px;color:#fff}

/* letterhead */
.letter{left:614px;top:89px;width:478px;height:677px}
.letter .wave{top:0;height:60px}
.letter .brand{position:absolute;left:76px;top:58px;font-size:22px;width:140px}
.letter .recipient{position:absolute;left:76px;top:168px;font-size:7px;line-height:1.5}
.letter .recipient strong{font-size:8px;font-weight:700}
.letter .body{position:absolute;left:76px;top:256px;width:326px;font-size:7.6px;line-height:1.95;font-weight:600;text-align:justify}
.letter .body p{margin-bottom:10px}
.letter .signoff{position:absolute;right:76px;top:545px;font-size:6.5px;font-weight:700}
.letter .signature{position:absolute;left:324px;top:556px;width:56px;height:48px;background:radial-gradient(ellipse at center,#d8d8d8,rgba(255,255,255,0) 70%)}
.letter .rule{position:absolute;left:76px;right:70px;top:623px;height:1px;background:#888}
.letter .footer{position:absolute;left:76px;top:630px;width:332px;display:flex;font-size:5.6px;line-height:1.35;font-weight:600}
.letter .footer .col{padding-right:14px}
.letter .footer .col + .col{border-left:1px solid var(--copper);padding-left:12px}
</style>
</head>
<body>

<section class="piece card-back">
  <div class="brand">Pelham Ridge Hospital</div>
</section>

<section class="piece card-front">
  <div class="brand">Pelham Ridge Hospital</div>
  <div class="divider"></div>
  <div class="info">
    <div class="name">Derek Solano</div>
    <div class="title">Chief Executive Officer</div>
    <div class="addr">382 Wilmot Street Box 415<br>Alder Springs, Westmark 76291</div>
    <div class="contact-row"><span class="dot"></span>325-740-2386 (Main)</div>
    <div class="contact-row"><span class="dot"></span>xxxxxxxxxx (Direct)</div>
    <div class="contact-row"><span class="dot"></span>xxxxxxxxxx</div>
    <div class="contact-row"><span class="dot"></span>derek.solano@pelhamrh.com</div>
    <div class="contact-row"><span class="dot"></span>www.pelhamrh.com</div>
  </div>
  <svg class="wave" viewBox="0 0 203 36" preserveAspectRatio="none">
    <path d="M0,36 V22 C40,6 90,2 130,10 C160,16 185,22 203,22 V36 Z" fill="var(--copper)"/>
    <path d="M90,4 C130,2 170,14 203,16 V22 C175,18 140,8 90,4 Z" fill="var(--ink)"/>
  </svg>
</section>

<section class="piece env-front">
  <div class="brand">Pelham Ridge Hospital</div>
  <div class="addr">382 Wilmot Street Box 415<br>Alder Springs, Westmark 76291</div>
  <svg class="wave" viewBox="0 0 480 62" preserveAspectRatio="none">
    <path d="M0,62 V28 C60,8 150,0 240,6 C330,12 410,34 480,40 V62 Z" fill="var(--copper)"/>
    <path d="M270,4 C350,8 420,24 480,22 V34 C420,32 350,14 270,4 Z" fill="var(--ink)"/>
  </svg>
</section>

<section class="piece env-back">
  <svg class="flap" viewBox="0 0 480 68" preserveAspectRatio="none">
    <path d="M0,0 H480 L446,68 H34 Z" fill="var(--copper)"/>
  </svg>
  <div class="brand">Pelham Ridge Hospital</div>
</section>

<section class="piece letter">
  <svg class="wave" viewBox="0 0 478 60" preserveAspectRatio="none">
    <path d="M0,0 H478 V56 C430,58 380,40 320,24 C240,4 150,8 0,16 Z" fill="var(--copper)"/>
    <path d="M0,16 C150,6 240,2 320,20 C250,10 150,14 0,26 Z" fill="var(--ink)"/>
  </svg>
  <div class="brand">Pelham Ridge Hospital</div>
  <div class="recipient">
    <strong>LOREM IPSUM DOLOR</strong><br>
    sim aciem perdaffres at ortantis.<br>
    Fas ipsantat omnem inatus<br>
    Marit. Atabunum iu maxim<br>
    troximant, ta acrit,
  </div>
  <div class="body">
    <p>Lorem ipsum dolor sit amet, consectetuer adipiscing elit. Aenean commodo ligula eget dolor. Aenean massa. Cum sociis natoque penatibus et magnis dis parturient montes, nascetur ridiculus mus. Donec quam felis, ultricies nec, pellentesque eu, pretium quis, sem. Nulla consequat massa quis enim. Donec pede justo, fringilla vel, aliquet nec, vulputate eget, arcu. In enim justo, rhoncus ut, imperdiet a, venenatis vitae, justo. Nullam dictum felis eu pede mollis pretium. Integer tincidunt. Cras dapibus. Vivamus elementum semper nisi. Aenean vulputate eleifend tellus. Aenean leo ligula, porttitor eu, consequat vitae, eleifend ac, enim. Aliquam lorem ante, dapibus in, viverra quis, feugiat a, tellus.</p>
    <p>Phasellus viverra nulla ut metus varius laoreet. Quisque rutrum. Aenean imperdiet. Etiam ultricies nisi vel augue. Curabitur ullamcorper ultricies nisi. Nam eget dui. Etiam rhoncus. Maecenas tempus, tellus eget condimentum rhoncus, sem quam semper libero, sit amet adipiscing sem neque sed ipsum. Nam quam nunc, blandit vel, luctus pulvinar, hendrerit id, lorem. Maecenas nec odio et ante tincidunt tempus. Donec vitae sapien ut libero venenatis faucibus. Nullam quis ante. Etiam sit amet orci eget eros faucibus tincidunt.</p>
    <p>Vestibulum purus quam, scelerisque ut, mollis sed, nonummy id, metus. Nullam accumsan lorem in dui. Cras ultricies mi eu turpis hendrerit fringilla. Vestibulum ante ipsum primis in faucibus orci luctus et ultrices posuere cubilia Curae;diet feugiatimperdiet,quis porttitor congue, elit erat euismod orci, ac</p>
  </div>
  <div class="signoff">Idetli namur</div>
  <div class="signature" role="img" aria-label="Handwritten signature of the sender"></div>
  <div class="rule"></div>
  <div class="footer">
    <div class="col">382 Wilmot Street Box 415<br>Alder Springs, Westmark 76291</div>
    <div class="col">
      <div class="contact-row"><span class="dot"></span>325-740-2386</div>
      <div class="contact-row"><span class="dot"></span>xxxxxx</div>
      <div class="contact-row"><span class="dot"></span>xxxxxx</div>
    </div>
    <div class="col">
      <div class="contact-row"><span class="dot"></span>derek.solano@pelhamrh.com</div>
      <div class="contact-row"><span class="dot"></span>www.pelhamrh.com</div>
    </div>
  </div>
</section>

</body>
</html>
```